2 Page Brochure - Commercial Roofing Company

We are looking for a double sided brochure, full color, for our commercial roofing company that tells customers a little bit about the company, what we do, and shows a few pictures.
The brochure would need to have our logo and color scheme that coordinates with that logo.
I have uploaded our logo, some ideas I had, and then the idea list also has our website on there if you'd like to take a look around there for some more ideas.
I have also uploaded some photos we'd like to use.
Page size should be 8.5" x 11".
Target Market(s)
Commercial Property Owners
Other font styles liked:
- Match logo font ideally so it's cohesive, but whatever looks best
Look and feel

```html
<!DOCTYPE html>
<html lang="en">
<head>
<meta charset="utf-8">
<title>Copperline Roofing – Commercial Brochure</title>
<link href="https://fonts.googleapis.com/css2?family=Bebas+Neue&family=Montserrat:wght@400;500;600;700;800&display=swap" rel="stylesheet">
<style>
  :root{
    --orange:#f15a22;
    --black:#0a0a0a;
    --ink:#1c2230;
    --white:#ffffff;
    --mat:#6e6e6e;
    --mist:#eceef1;
    --gold:#c9a45a;
  }
  *{box-sizing:border-box;margin:0;padding:0}
  html,body{width:1200px;height:821px;overflow:hidden;background:var(--mat)}
  body{position:relative;font-family:"Montserrat",Arial,sans-serif}
  .page{position:absolute;top:66px;width:493px;height:690px;background:var(--white);overflow:hidden}
  .page--front{left:71px}
  .page--back{left:636px}
  .page__shapes{position:absolute;inset:0}
  .page > *:not(.page__shapes){position:absolute}

  .brand{left:27px;top:36px;width:194px;text-align:center;color:var(--ink);font-weight:800;line-height:1}
  .brand__top{display:block;font-size:25px;letter-spacing:.5px}
  .brand__bottom{display:block;font-size:27px;letter-spacing:1px;margin-top:4px}

  .display{font-family:"Bebas Neue",Impact,sans-serif;font-weight:400;line-height:.92;color:var(--white)}
  .accent{color:var(--orange)}

  .specialty-tag{left:27px;top:148px;width:222px;height:27px;background:var(--orange);color:var(--white);
    font-weight:800;font-size:19px;text-align:center;line-height:27px;letter-spacing:.3px}
  .headline-main{left:25px;top:176px;font-size:57px}
  .headline-big{left:22px;top:226px;font-size:124px;color:var(--orange);line-height:.9}

  .intro{left:21px;top:358px;width:335px;font-size:10.6px;line-height:13.4px;color:var(--white);text-align:justify}

  .services{left:21px;top:433px;width:247px;height:186px;background:var(--black);border-radius:12px 12px 0 0;padding:14px 0 0 8px}
  .services__title{font-size:34px;line-height:.92}
  .checklist{list-style:none;color:var(--white)}
  .services .checklist{margin-top:9px;font-size:13.4px;line-height:19px}
  .checklist li{display:flex;align-items:center;gap:5px;white-space:nowrap}
  .tick{width:11px;height:11px;flex:none}

  .photo{border-radius:50%;border:5px solid var(--white)}
  .photo--roof{left:323px;top:397px;width:124px;height:124px;background:linear-gradient(160deg,#c9d6de 0%,#f4f6f8 45%,#9aa0a6 100%)}
  .photo--storefront{left:356px;top:475px;width:128px;height:128px;background:linear-gradient(180deg,#8ea3c0 0%,#b88a6a 45%,#4d4f55 100%)}
  .badge{left:278px;top:487px;width:104px;height:104px;border-radius:50%;background:var(--white);border:5px solid var(--mist);display:flex;align-items:center;justify-content:center}
  .badge__mark{width:48px;height:48px;border:2px solid var(--gold)}

  .cta-label{left:21px;top:630px;font-size:12.5px;font-weight:800;color:var(--ink)}
  .phone{left:20px;top:646px;font-size:28px;font-weight:700;color:var(--orange);letter-spacing:-.3px}
  .license{right:24px;top:639px;font-size:13.5px;font-weight:600;color:var(--orange)}
  .web{right:24px;top:656px;font-size:10px;font-weight:700;color:var(--ink)}

  .installs{left:36px;top:150px;font-size:36px}
  .installs-list{left:36px;top:211px;display:grid;grid-template-columns:127px 110px;font-size:11.3px;line-height:19px}
  .coverage{left:33px;top:320px;font-size:32px;line-height:.92}
  .about{left:33px;top:381px;width:431px;font-size:9.3px;line-height:13.4px;color:var(--white);text-align:justify}
  .about p + p{margin-top:10px}
  .makers-title{left:36px;top:545px;font-size:28px;color:var(--ink)}
  .makers{left:30px;top:583px;width:440px;height:44px;display:flex;align-items:center;justify-content:space-between}
  .maker{background:#b8bec7}
  .maker--round{width:44px;height:44px;border-radius:50%;background:#2f3d7a}
  .maker--wide{width:78px;height:34px;background:#d7dbe1}
  .maker--diamond{width:34px;height:34px;transform:rotate(45deg);background:#c7c9cc;border:3px solid #c0272d}
  .maker--tile{width:72px;height:16px;background:#8c8f94}
  .maker--bar{width:70px;height:22px;background:#2f5fae}
  .maker--stack{width:70px;height:24px;background:#3b4f6b}
  .phone--dark{color:var(--black);left:33px;font-size:29px}
  .web--back{right:30px;top:652px;font-size:11px}
</style>
</head>
<body>

<section class="page page--front" aria-label="Brochure front page">
  <svg class="page__shapes" width="493" height="690" viewBox="0 0 493 690" aria-hidden="true">
    <rect x="0" y="123" width="493" height="223" fill="var(--black)"/>
    <rect x="0" y="345" width="493" height="275" fill="var(--orange)"/>
    <circle cx="471" cy="167" r="218" fill="var(--orange)"/>
  </svg>
  <svg class="page__shapes" width="493" height="690" viewBox="0 0 493 690" role="img" aria-label="Photo of a newly roofed single-storey commercial building with brick base and an empty parking lot under a cloudy sky">
    <defs>
      <linearGradient id="frontPhoto" x1="0" y1="0" x2="0" y2="1">
        <stop offset="0" stop-color="#cfd9e4"/>
        <stop offset=".35" stop-color="#9eaec0"/>
        <stop offset=".55" stop-color="#4a4c52"/>
        <stop offset=".7" stop-color="#6b5f5a"/>
        <stop offset="1" stop-color="#58534f"/>
      </linearGradient>
    </defs>
    <circle cx="471" cy="167" r="209" fill="url(#frontPhoto)"/>
  </svg>

  <div class="brand"><span class="brand__top">COPPERLINE</span><span class="brand__bottom">ROOFING</span></div>

  <div class="specialty-tag">OUR SPECIALTY IS</div>
  <h1 class="display headline-main">COMMERCIAL</h1>
  <div class="display headline-big">ROOFS</div>

  <p class="intro">Copperline Roofing opened the doors in 1984, and we’ve since installed, serviced, maintained, and coated thousands of commercial roofs around the state of Arizona, in the many climate regions of the state.</p>

  <div class="services">
    <h2 class="display services__title">COPPERLINE ROOFING<br>SERVICES:</h2>
    <ul class="checklist">
      <li><svg class="tick" viewBox="0 0 12 12"><circle cx="6" cy="6" r="5" fill="none" stroke="var(--orange)" stroke-width="1.4"/><path d="M3.4 6.2l2 2 4.5-5" fill="none" stroke="var(--orange)" stroke-width="1.8" stroke-linecap="round"/></svg>New Roof Installation</li>
      <li><svg class="tick" viewBox="0 0 12 12"><circle cx="6" cy="6" r="5" fill="none" stroke="var(--orange)" stroke-width="1.4"/><path d="M3.4 6.2l2 2 4.5-5" fill="none" stroke="var(--orange)" stroke-width="1.8" stroke-linecap="round"/></svg>Re-roofing</li>
      <li><svg class="tick" viewBox="0 0 12 12"><circle cx="6" cy="6" r="5" fill="none" stroke="var(--orange)" stroke-width="1.4"/><path d="M3.4 6.2l2 2 4.5-5" fill="none" stroke="var(--orange)" stroke-width="1.8" stroke-linecap="round"/></svg>Roof Maintenance and Service</li>
      <li><svg class="tick" viewBox="0 0 12 12"><circle cx="6" cy="6" r="5" fill="none" stroke="var(--orange)" stroke-width="1.4"/><path d="M3.4 6.2l2 2 4.5-5" fill="none" stroke="var(--orange)" stroke-width="1.8" stroke-linecap="round"/></svg>Roof Inspections</li>
      <li><svg class="tick" viewBox="0 0 12 12"><circle cx="6" cy="6" r="5" fill="none" stroke="var(--orange)" stroke-width="1.4"/><path d="M3.4 6.2l2 2 4.5-5" fill="none" stroke="var(--orange)" stroke-width="1.8" stroke-linecap="round"/></svg>Roof Coatings</li>
    </ul>
  </div>

  <div class="photo photo--roof" role="img" aria-label="Photo of a white coated flat commercial roof with rooftop units"></div>
  <div class="badge" role="img" aria-label="Contractor certification badge"><div class="badge__mark"></div></div>
  <div class="photo photo--storefront" role="img" aria-label="Photo of a brick restaurant building with metal parapet at dusk"></div>

  <div class="cta-label">CALL US NOW TODAY!</div>
  <div class="phone">555-010-4800</div>
  <div class="license">AZ ROC 120456</div>
  <div class="web">www.copperline-roofing.com</div>
</section>

<section class="page page--back" aria-label="Brochure back page">
  <svg class="page__shapes" width="493" height="690" viewBox="0 0 493 690" aria-hidden="true">
    <rect x="0" y="123" width="493" height="187" fill="var(--black)"/>
    <rect x="0" y="309" width="493" height="229" fill="var(--orange)"/>
    <rect x="0" y="537" width="493" height="101" fill="var(--mist)"/>
    <circle cx="471" cy="167" r="218" fill="var(--orange)"/>
  </svg>
  <svg class="page__shapes" width="493" height="690" viewBox="0 0 493 690" role="img" aria-label="Photo of a standing seam metal roof below a restaurant facade against a clear blue sky">
    <defs>
      <linearGradient id="backPhoto" x1="0" y1="0" x2="0" y2="1">
        <stop offset="0" stop-color="#4f8fd6"/>
        <stop offset=".3" stop-color="#a9c3da"/>
        <stop offset=".5" stop-color="#7f9f98"/>
        <stop offset="1" stop-color="#5d7f78"/>
      </linearGradient>
    </defs>
    <circle cx="471" cy="167" r="209" fill="url(#backPhoto)"/>
  </svg>

  <div class="brand"><span class="brand__top">COPPERLINE</span><span class="brand__bottom">ROOFING</span></div>

  <h2 class="display installs">COPPERLINE ROOFING<br><span class="accent">INSTALLS:</span></h2>
  <ul class="checklist installs-list">
    <li><svg class="tick" viewBox="0 0 12 12"><circle cx="6" cy="6" r="5" fill="none" stroke="var(--orange)" stroke-width="1.4"/><path d="M3.4 6.2l2 2 4.5-5" fill="none" stroke="var(--orange)" stroke-width="1.8" stroke-linecap="round"/></svg>TPO</li>
    <li><svg class="tick" viewBox="0 0 12 12"><circle cx="6" cy="6" r="5" fill="none" stroke="var(--orange)" stroke-width="1.4"/><path d="M3.4 6.2l2 2 4.5-5" fill="none" stroke="var(--orange)" stroke-width="1.8" stroke-linecap="round"/></svg>Acrylic Coatings</li>
    <li><svg class="tick" viewBox="0 0 12 12"><circle cx="6" cy="6" r="5" fill="none" stroke="var(--orange)" stroke-width="1.4"/><path d="M3.4 6.2l2 2 4.5-5" fill="none" stroke="var(--orange)" stroke-width="1.8" stroke-linecap="round"/></svg>PVC</li>
    <li><svg class="tick" viewBox="0 0 12 12"><circle cx="6" cy="6" r="5" fill="none" stroke="var(--orange)" stroke-width="1.4"/><path d="M3.4 6.2l2 2 4.5-5" fill="none" stroke="var(--orange)" stroke-width="1.8" stroke-linecap="round"/></svg>Shingle</li>
    <li><svg class="tick" viewBox="0 0 12 12"><circle cx="6" cy="6" r="5" fill="none" stroke="var(--orange)" stroke-width="1.4"/><path d="M3.4 6.2l2 2 4.5-5" fill="none" stroke="var(--orange)" stroke-width="1.8" stroke-linecap="round"/></svg>Modified Bitumen</li>
    <li><svg class="tick" viewBox="0 0 12 12"><circle cx="6" cy="6" r="5" fill="none" stroke="var(--orange)" stroke-width="1.4"/><path d="M3.4 6.2l2 2 4.5-5" fill="none" stroke="var(--orange)" stroke-width="1.8" stroke-linecap="round"/></svg>Metal</li>
    <li><svg class="tick" viewBox="0 0 12 12"><circle cx="6" cy="6" r="5" fill="none" stroke="var(--orange)" stroke-width="1.4"/><path d="M3.4 6.2l2 2 4.5-5" fill="none" stroke="var(--orange)" stroke-width="1.8" stroke-linecap="round"/></svg>Silicone Coatings</li>
    <li><svg class="tick" viewBox="0 0 12 12"><circle cx="6" cy="6" r="5" fill="none" stroke="var(--orange)" stroke-width="1.4"/><path d="M3.4 6.2l2 2 4.5-5" fill="none" stroke="var(--orange)" stroke-width="1.8" stroke-linecap="round"/></svg>Tile</li>
  </ul>

  <h2 class="display coverage">WE SERVICE THE ENTIRE<br>STATE OF ARIZONA.</h2>
  <div class="about">
    <p>Though we all live here for the constant sunshine, Arizona is one of the harshest environments in the US for roofs. Constant sun, heat, dryness, and then the torrential monsoon downpours all test the limits of your roof.</p>
    <p>We work with you to come up with a solution that works for your roof and will keep your business dry for years to come. Then, our team of project managers, superintendents, foremen, and field workers all come together to execute on that plan and install a quality roof.</p>
    <p>We are certified with many different manufacturers, so we’re able to offer custom solutions to solve your issues, that will also often come with reputable manufacturer warranties.</p>
  </div>

  <h2 class="display makers-title">CERTIFIED MANUFACTURERS:</h2>
  <div class="makers" role="img" aria-label="Row of certified manufacturer badges">
    <span class="maker maker--round"></span>
    <span class="maker maker--wide"></span>
    <span class="maker maker--diamond"></span>
    <span class="maker maker--tile"></span>
    <span class="maker maker--bar"></span>
    <span class="maker maker--stack"></span>
  </div>

  <div class="phone phone--dark">555-010-4800</div>
  <div class="web web--back">www.copperline-roofing.com</div>
</section>

</body>
</html>
```